SKYBEND FITNESSRoll Out, A UNIQUE CONCIERGE MOBILE SERVICE LAUNCHING in SOUTH FLORIDA

I AM LOOKING TO ATTRACT LEADS FOR CONVERSION WHILE BRINGING OUR SERVICE TO LIFE IN THERE HANDS. WE SERVICE A VERY HIGHLY AFFLUENT CROWD. I would like those on a 5 x 7 two sided card

Target Market(s)

AFFLUENT

Industry/Entity Type

HEALTH AND FITNESS

Font styles to use
Other font styles liked:
• POPINS MED

Colors
0054AA
0677BA
7BADD7
CADEEF
E8F1F8
FFF300
FFF600
FEFA6F
FFFEC7
FFFEE8

Requirements
Must have
• space for postage I INCLUDED CONTENT
Nice to have
• CLASSY FUN LOOK
Should not have
• DULLNESs

```html
<!DOCTYPE html>
<html lang="en">
<head>
<meta charset="utf-8">
<title>SkyBend Fitness – Two-Sided Card</title>
<link href="https://fonts.googleapis.com/css2?family=Poppins:wght@400;500;600;700;800;900&display=swap" rel="stylesheet">
<style>
  :root{
    --navy:#1c2940;
    --navy-deep:#142036;
    --teal:#5ccfe0;
    --yellow:#ffe600;
    --yellow-brush:#f2e21a;
    --blue:#0054aa;
    --ink:#14213a;
    --white:#ffffff;
    --page:#ffffff;
    --rule:#c9d3e3;
  }
  *{margin:0;padding:0;box-sizing:border-box}
  html,body{width:821px;height:1200px;overflow:hidden;background:var(--page)}
  body{position:relative;font-family:"Poppins",sans-serif}
  .card{position:absolute;top:326px;width:390px;height:547px;overflow:hidden;box-shadow:0 4px 14px rgba(0,0,0,.28)}
  .card--front{left:14px}
  .card--back{left:417px}
  .card__art{position:absolute;inset:0;width:390px;height:547px}
  .brand{position:absolute;top:16px;left:0;width:100%;text-align:center}
  .brand__name{display:block;font-family:"Poppins",sans-serif;font-weight:600;font-size:44px;line-height:50px;color:var(--teal);letter-spacing:2px}
  .brand__tagline{display:block;font-weight:700;font-size:8.5px;letter-spacing:6px;color:var(--yellow);margin-top:2px}
  .headline{position:absolute;left:0;width:100%;text-align:center;font-weight:800}
  .headline--main{top:92px;font-size:74px;line-height:80px;color:var(--white);letter-spacing:-1px}
  .headline--sub{top:170px;font-size:32px;line-height:38px;color:var(--teal);letter-spacing:-.3px}
  .brush-text{position:absolute;font-weight:800;color:var(--ink);white-space:nowrap}
  .brush-text--front{left:52px;top:232px;font-size:27px;transform:rotate(-5deg);transform-origin:left center}
  .web{position:absolute;font-weight:700;white-space:nowrap}
  .web--front{right:26px;bottom:18px;font-size:8.5px;letter-spacing:1.3px;color:var(--white)}
  .pitch{position:absolute;left:0;top:286px;width:100%;text-align:center;font-weight:800;font-size:19.5px;line-height:21px;color:var(--blue)}
  .brush-text--back{left:50px;top:350px;font-size:28.5px;transform:rotate(-2deg);transform-origin:left center}
  .services{position:absolute;left:17px;top:418px;width:356px;height:72px;border:1px dashed #7f9bc8;border-radius:6px}
  .services__title{position:absolute;top:-8px;left:50%;transform:translateX(-50%);background:var(--white);padding:0 4px;font-weight:700;font-size:9.5px;line-height:14px;color:var(--blue);white-space:nowrap}
  .services__list{position:absolute;left:4px;right:4px;top:14px;display:flex;list-style:none}
  .service{flex:1;display:flex;flex-direction:column;align-items:center;border-left:1px solid var(--rule);padding-top:0}
  .service:first-child{border-left:none}
  .service__icon{width:24px;height:24px}
  .service__label{margin-top:7px;font-weight:600;font-size:7.6px;color:var(--ink);letter-spacing:.2px}
  .cta{position:absolute;left:18px;top:512px;font-size:6.8px;line-height:9px;color:var(--ink)}
  .cta strong{font-weight:700;display:block}
  .web--back{right:26px;top:512px;font-size:11px;color:var(--ink)}
  .web--back .web__accent{color:var(--teal)}
</style>
</head>
<body>

<section class="card card--front" aria-label="Card front">
  <svg class="card__art" viewBox="0 0 390 547" aria-hidden="false">
    <defs>
      <linearGradient id="frontPhoto" x1="0" y1="0" x2="1" y2="1">
        <stop offset="0" stop-color="#4b4c50"/>
        <stop offset=".55" stop-color="#2f3033"/>
        <stop offset="1" stop-color="#555350"/>
      </linearGradient>
    </defs>
    <rect width="390" height="547" fill="var(--navy)"/>
    <polygon points="0,305 390,255 390,547 0,547" fill="var(--yellow)"/>
    <g role="img" aria-label="Photo of trainers exercising with resistance bands beside the branded fitness truck">
      <polygon points="80,292 390,240 390,547 40,547" fill="url(#frontPhoto)"/>
    </g>
    <polygon points="0,480 0,547 36,547 390,385 390,355" fill="var(--teal)"/>
    <polygon points="0,470 0,480 390,355 390,345" fill="var(--navy)" opacity=".0"/>
    <polygon points="45,240 360,212 372,226 356,236 368,250 340,258 40,286 26,276 44,266 30,256" fill="var(--yellow-brush)"/>
  </svg>

  <div class="brand">
    <span class="brand__name">SKYBEND</span>
    <span class="brand__tagline">MOVING YOUR WAY</span>
  </div>
  <h1 class="headline headline--main">GET FIT</h1>
  <p class="headline headline--sub">ON YOUR SCHEDULE</p>
  <p class="brush-text brush-text--front">ANYWHERE, ANYTIME</p>
  <p class="web web--front">www.skybendfitness.com</p>
</section>

<section class="card card--back" aria-label="Card back">
  <svg class="card__art" viewBox="0 0 390 547">
    <defs>
      <linearGradient id="backPhoto" x1="0" y1="0" x2="1" y2="0">
        <stop offset="0" stop-color="#d8d22e"/>
        <stop offset=".35" stop-color="#8f8c52"/>
        <stop offset=".6" stop-color="#5e5f62"/>
        <stop offset="1" stop-color="#8a8b8e"/>
      </linearGradient>
    </defs>
    <rect width="390" height="547" fill="var(--navy)"/>
    <polygon points="0,93 390,79 390,310 0,310" fill="var(--yellow)"/>
    <g role="img" aria-label="Photo of the branded fitness truck with training straps on a rooftop lot">
      <polygon points="60,90 390,79 390,312 0,312 0,230" fill="url(#backPhoto)"/>
    </g>
    <polygon points="0,262 0,312 14,312 390,86 390,79" fill="var(--teal)"/>
    <polygon points="0,312 390,300 390,547 0,547" fill="var(--white)"/>
    <polygon points="20,352 360,336 376,346 362,356 372,368 350,378 30,392 10,384 28,376 12,366" fill="var(--yellow-brush)"/>
  </svg>

  <div class="brand">
    <span class="brand__name">SKYBEND</span>
    <span class="brand__tagline">MOVING YOUR WAY</span>
  </div>
  <h2 class="pitch">TRANSFORM YOUR<br>BODY AND YOUR GAME WITH</h2>
  <p class="brush-text brush-text--back">SKYBEND FITNESS</p>

  <div class="services">
    <p class="services__title">THE ULTIMATE MOBILE CONCIERGE FITNESS SERVICE FOR</p>
    <ul class="services__list">
      <li class="service">
        <svg class="service__icon" viewBox="0 0 24 24"><circle cx="12" cy="12" r="12" fill="var(--teal)"/><path d="M12 17l-4.5-4.3a2.6 2.6 0 0 1 4.5-2.9 2.6 2.6 0 0 1 4.5 2.9z" fill="#fff"/></svg>
        <span class="service__label">HEALTH</span>
      </li>
      <li class="service">
        <svg class="service__icon" viewBox="0 0 24 24"><circle cx="12" cy="12" r="12" fill="var(--teal)"/><path d="M10 6v11M10 6l6 2.5-6 2.5" stroke="#fff" stroke-width="1.6" fill="#fff"/><ellipse cx="12" cy="17.5" rx="4" ry="1.2" fill="#fff"/></svg>
        <span class="service__label">GOLF</span>
      </li>
      <li class="service">
        <svg class="service__icon" viewBox="0 0 24 24"><circle cx="12" cy="12" r="12" fill="var(--teal)"/><ellipse cx="11" cy="10" rx="3.5" ry="4" fill="none" stroke="#fff" stroke-width="1.6"/><path d="M13 13.5l3.5 4" stroke="#fff" stroke-width="1.8"/><circle cx="16.5" cy="8" r="1.5" fill="#fff"/></svg>
        <span class="service__label">TENNIS</span>
      </li>
      <li class="service">
        <svg class="service__icon" viewBox="0 0 24 24"><circle cx="12" cy="12" r="12" fill="var(--teal)"/><circle cx="12" cy="6.8" r="1.6" fill="#fff"/><path d="M6 10.5h12M12 10v4M12 14l-4 4M12 14l4 4" stroke="#fff" stroke-width="1.6" stroke-linecap="round"/></svg>
        <span class="service__label">FLEXIBILITY</span>
      </li>
      <li class="service">
        <svg class="service__icon" viewBox="0 0 24 24"><circle cx="12" cy="12" r="12" fill="var(--teal)"/><path d="M8 16l8-8" stroke="#fff" stroke-width="1.6"/><path d="M6 14l4 4M7.5 12.5l4 4M12.5 7.5l4 4M14 6l4 4" stroke="#fff" stroke-width="1.8" stroke-linecap="round"/></svg>
        <span class="service__label">STRENGTH</span>
      </li>
      <li class="service">
        <svg class="service__icon" viewBox="0 0 24 24"><circle cx="12" cy="12" r="12" fill="var(--teal)"/><circle cx="14.5" cy="6.5" r="1.6" fill="#fff"/><path d="M9 9.5l4-1 2 4 3 1M13 8.5l-2 5-3 4M11 13.5l3 1.5-1 3.5" stroke="#fff" stroke-width="1.6" fill="none" stroke-linecap="round" stroke-linejoin="round"/></svg>
        <span class="service__label">AGILITY</span>
      </li>
    </ul>
  </div>

  <p class="cta">Get Started with SkyBend Fitness Today<strong>FOR FREE CONSULTAION AND ASSESMENT GO TO</strong></p>
  <p class="web web--back">www.<span class="web__accent">skybendfitness</span>.com</p>
</section>

</body>
</html>
```